Gutschein-Design Falter Webshop
Zielgruppe
Webshop von Pyrotechnischen Artikeln. Rauchkörper, Bengalische Lichter, Kinderfeuerwerk, klassisches Silvesterfeuerwerk. Der Shop ist zu finden unter https://www.funkenkiste-beispiel.de
Das Format sollte sich an DIN Lang orientieren.
Wenn Artikelbilder oder sonstige Fotos aus dem Shop benötigt werden, können diese gerne angefragt werden.
Aufgabenstellung
Der Shop sollte im Flyer wieder erkennbar sein und nach Möglichkeit alle 5 Hauptkategorien abbilden.
Wobei Silvesterfeuerwerk, Zubehör und Partyartikel die kleinere Rolle spielen.
Rauch und Bengal stehen dabei im Vordergrund
Ein Textfeld sollte enthalten sein, worein wir dann den Gutscheincode / Wert drucken.
Edit: Sorry, ich hatte anfangs die falschen Grafiken hochgeladen. Jetzt ist das Shoplogo in den Files zu finden. Ebenso ein Beispielfoto mit Rauch

```html
<!DOCTYPE html>
<html lang="de">
<head>
<meta charset="utf-8">
<title>Gutschein – Funkenkiste</title>
<link rel="stylesheet" href="https://fonts.googleapis.com/css2?family=Archivo+Black&family=Open+Sans:wght@300;400;600;700&display=swap">
<style>
  :root {
    --orange: #f0930e;
    --orange-light: #fbb040;
    --gold: #c8963e;
    --ink: #555a60;
    --grey-bg: #ededed;
    --white: #ffffff;
    --pink: #d8306a;
  }
  * { margin: 0; padding: 0; box-sizing: border-box; }
  html, body { width: 1016px; height: 1200px; overflow: hidden; background: var(--white); }
  body { font-family: "Open Sans", sans-serif; color: var(--ink); position: relative; }

  .brand-name {
    position: absolute;
    font-family: "Open Sans", sans-serif;
    font-weight: 600;
    color: var(--gold);
    display: flex; align-items: center; gap: 8px;
    letter-spacing: 0.5px;
  }
  .brand-name .brand-dot { width: 12px; height: 12px; background: var(--gold); }
  .brand-name--header { left: 47px; top: 62px; font-size: 32px; }
  .brand-name--card { left: 742px; top: 796px; font-size: 28px; }

  .shop-nav {
    position: absolute; left: 305px; top: 76px; right: 0; height: 42px;
    border-bottom: 2px solid var(--orange);
    display: flex; align-items: flex-end;
  }
  .shop-nav__item {
    font-size: 17px; color: #555e6a; padding: 0 16px 9px; margin-right: 1px;
  }
  .shop-nav__item--active {
    background: linear-gradient(var(--orange-light), var(--orange));
    color: var(--white); font-weight: 700; border-radius: 3px 3px 0 0;
    padding: 10px 14px 9px;
  }

  .smoke-banner {
    position: absolute; left: 0; top: 180px; width: 1016px; height: 300px;
    background:
      linear-gradient(to bottom, rgba(255,255,255,1) 0%, rgba(255,255,255,0.55) 35%, rgba(255,255,255,0) 65%),
      linear-gradient(to right, #d7a21a 0%, #e8a84a 25%, #ea7a5a 50%, #d9405a 72%, #e2709e 100%);
  }
  .title-word {
    position: absolute;
    font-family: "Archivo Black", sans-serif;
    line-height: 1;
    letter-spacing: -1px;
  }
  .title-word--banner { left: 47px; top: 345px; font-size: 104px; color: var(--white); }

  .voucher-card {
    position: absolute; left: 0; top: 717px; width: 1016px; height: 483px;
    background: var(--grey-bg);
  }
  .voucher-card__photo {
    position: absolute; inset: 0;
    background:
      radial-gradient(ellipse at 48% 45%, rgba(255,255,255,0.95) 0%, rgba(255,255,255,0.4) 35%, rgba(255,255,255,0) 70%),
      var(--grey-bg);
  }
  .claim-box {
    position: absolute; left: 62px; top: 0; width: 275px; height: 152px;
    background: var(--orange); border-radius: 0 0 6px 6px;
    color: var(--white); font-weight: 300; font-size: 30px; line-height: 36px;
    padding: 63px 0 0 16px;
  }
  .claim-box span { display: block; }
  .claim-box span + span { padding-left: 25px; }
  .value-label {
    position: absolute; left: 242px; top: 180px;
    color: var(--orange); font-weight: 700; font-size: 14.5px;
  }
  .shop-url {
    position: absolute; right: 29px; top: 280px;
    font-size: 20px; font-weight: 300; color: #666;
  }
  .contact {
    position: absolute; right: 29px; top: 335px;
    text-align: right; font-size: 12.5px; line-height: 16.4px; color: #666;
  }
  .contact p + p { margin-top: 16px; }
  .title-word--card {
    left: 44px; top: 355px; font-size: 100px;
    background: linear-gradient(to right, #d9a01e 0%, #ea9440 35%, #e85a50 60%, #e02c5a 80%, #e6407e 100%);
    -webkit-background-clip: text; background-clip: text; color: transparent;
  }
</style>
</head>
<body>
  <header>
    <div class="brand-name brand-name--header"><span>funkenkiste</span><span class="brand-dot"></span></div>
    <nav class="shop-nav">
      <span class="shop-nav__item shop-nav__item--active">Bengal</span>
      <span class="shop-nav__item">Rauchkörper</span>
      <span class="shop-nav__item">Partyartikel</span>
      <span class="shop-nav__item">Feuerwerk</span>
      <span class="shop-nav__item">Zubehör</span>
      <span class="shop-nav__item">Informationen</span>
    </nav>
  </header>

  <div class="smoke-banner" role="img" aria-label="Farbiger Rauch in Gelb, Orange und Pink"></div>
  <div class="title-word title-word--banner">Gutschein</div>

  <section class="voucher-card">
    <div class="voucher-card__photo" role="img" aria-label="Helle Funken einer Wunderkerze auf grauem Grund"></div>
    <div class="claim-box"><span>Erleben Sie</span><span>den Unterschied.</span></div>
    <div class="value-label">Im Wert von:</div>
    <div class="brand-name brand-name--card" style="top:79px"><span>funkenkiste</span><span class="brand-dot"></span></div>
    <div class="shop-url">www.funkenkiste-beispiel.de</div>
    <div class="contact">
      <p>Lindner &amp; Haas GbR<br>Birkenweg 12<br>15570 Seeheim</p>
      <p>Telefon: 03371.402816<br>Telefax: 03371.402817<br>E-Mail: info@funkenkiste-beispiel.de</p>
    </div>
    <div class="title-word title-word--card">Gutschein</div>
  </section>
</body>
</html>
```